Electrician Needs A Business Card

I already have a logo and would like a business card to be designed based around this logo the company is called Tolvane Electrical Pty Ltd

The business card will be printed on transparent plastic so I need it to stand out from the crowd. I do not want the card to have anything to do with Electrical on it eg light bulbs, power points etc

I need it to have the following details.

Gareth Pomfrey
Mobile : 0437 519 284
email : gareth@tolvaneelectrical.com.au

If it could incorporate the following onto the bottom of the card
ELECTRICAL - COMMUNICATIONS - AUDIO - VISUAL

```html
<!DOCTYPE html>
<html lang="en">
<head>
<meta charset="UTF-8">
<title>Tolvane Electrical – Business Card</title>
<link href="https://fonts.googleapis.com/css2?family=Lato:wght@400;700&display=swap" rel="stylesheet">
<style>
  :root {
    --backdrop: #6e6e6e;
    --card: #ffffff;
    --ink: #1a1a1a;
    --band: #111111;
    --accent: #f2a71b;
    --art-light: #fdf8d2;
    --art-mid: #f6ea7a;
  }
  * { box-sizing: border-box; margin: 0; padding: 0; }
  html, body {
    width: 1200px;
    height: 900px;
    overflow: hidden;
    background: var(--backdrop);
    font-family: "Lato", sans-serif;
  }
  .business-card {
    position: absolute;
    left: 100px;
    top: 144px;
    width: 1000px;
    height: 612px;
    background: var(--card);
    overflow: hidden;
  }
  .brand {
    position: absolute;
    left: 60px;
    top: 72px;
    display: flex;
    align-items: center;
    gap: 22px;
  }
  .brand-square {
    width: 100px;
    height: 100px;
    background: var(--accent);
  }
  .brand-name {
    font-size: 40px;
    font-weight: 400;
    color: var(--ink);
    letter-spacing: 0.5px;
  }
  .contact {
    position: absolute;
    left: 60px;
    top: 270px;
    color: var(--ink);
  }
  .contact-name {
    font-size: 44px;
    font-weight: 400;
    margin-bottom: 34px;
  }
  .contact-line {
    font-size: 29px;
    line-height: 1.45;
    letter-spacing: 0.5px;
  }
  .feature-art {
    position: absolute;
    left: 720px;
    top: 150px;
    width: 250px;
    height: 340px;
    background: linear-gradient(160deg, var(--art-light), var(--art-mid));
  }
  .service-band {
    position: absolute;
    left: 0;
    bottom: 0;
    width: 100%;
    height: 96px;
    background: var(--band);
    display: flex;
    align-items: center;
    justify-content: center;
    gap: 22px;
    color: var(--accent);
    font-size: 30px;
    font-weight: 700;
    letter-spacing: 2px;
  }
  .service-dot {
    width: 14px;
    height: 14px;
  }
</style>
</head>
<body>
  <main class="business-card">
    <div class="brand">
      <div class="brand-square"></div>
      <div class="brand-name">TOLVANE ELECTRICAL</div>
    </div>

    <section class="contact">
      <h1 class="contact-name">Gareth Pomfrey</h1>
      <p class="contact-line">M : 0437 519 284</p>
      <p class="contact-line">E : gareth@tolvaneelectrical.com.au</p>
    </section>

    <div class="feature-art" role="img" aria-label="Area for a yellow decorative illustration"></div>

    <footer class="service-band">
      <span>ELECTRICAL</span>
      <svg class="service-dot" viewBox="0 0 14 14" aria-hidden="true"><circle cx="7" cy="7" r="6" fill="var(--accent)"/></svg>
      <span>COMMUNICATIONS</span>
      <svg class="service-dot" viewBox="0 0 14 14" aria-hidden="true"><circle cx="7" cy="7" r="6" fill="var(--accent)"/></svg>
      <span>AUDIO</span>
      <svg class="service-dot" viewBox="0 0 14 14" aria-hidden="true"><circle cx="7" cy="7" r="6" fill="var(--accent)"/></svg>
      <span>VISUAL</span>
    </footer>
  </main>
</body>
</html>
```